Brochure for a civil enineering company in A4 format

I need a brochure design for our company TALVI Engineering S.r.l.. We are an engineering consultant company. Our main clients are from the infrastructure industry (geotechnical and underground sectors mainly).
We are looking for a 2 pages (4 faces) fold out design with a glued pocket where we can put individual data sheets.
I need A4 format pages.

Target Market(s)

We are an engineering consultant company. Our main clients are from the infrastructure industry (geotechnical and underground sectors mainly).

Industry/Entity Type

Civil Engineer

Font styles to use
Sans Serif

Requirements
Must have
• Overall: 2 pages in A4 format
Essential style. Bright and modern appearance.
Glued pocket
Logo integrated in a picture on the pocket where I would like to insert a slogan (… talvi engineering … reliable solutions …)
Attached are selected images which the designer can use and edit at their own discretion.
Some advice in the following (anyway designers are free to provide their solutions):
Outer sheets:
Front page with name, logo. It could be nice to have the “m” of the logo integrated in a pictures, also a modified picture (I mean modify one of the attached pictures) so to create a general image and do not tie the cover to a specific job.
Back page: offices address and contact email address. Nice to have one space for a slogan.
Inner sheet: text that I upload in the file “inside-sheets”, possibly with pictures on each sheet. In the right faces insert the glued pocket. On this pages insert the section OUR EXPERIENCE ….with a space for a picture of our team.
Nice to have
• Clean and essential design.
Pictures choosing from the atteched ones. Pictures could be modified in a very light manner to make them a general idea of the work ( I mean geotechnical world) without to be immediately linked to a specific site.
Should not have
• excessive frills

```html
<!DOCTYPE html>
<html lang="it">
<head>
<meta charset="utf-8">
<title>TALVI Engineering S.r.l. – Brochure</title>
<link href="https://fonts.googleapis.com/css2?family=Source+Sans+3:ital,wght@0,400;0,600;1,400&display=swap" rel="stylesheet">
<style>
  :root{
    --backdrop:#dcdcde;
    --paper:#ffffff;
    --navy:#23242f;
    --navy-soft:#2c2e3a;
    --mark-grey:#cfd0d4;
    --red:#c8202f;
    --ink:#1b1b1f;
    --body:#2a2a30;
  }
  *{margin:0;padding:0;box-sizing:border-box}
  html,body{width:1199px;height:1200px;overflow:hidden;background:var(--backdrop)}
  body{font-family:"Source Sans 3",sans-serif;color:var(--body)}
  .canvas{position:relative;width:1199px;height:1200px;overflow:hidden}
  .spread{position:absolute;left:48px;width:1098px;height:517px;background:var(--paper)}
  .spread--outer{top:37px}
  .spread--inner{top:632px}
  .spread svg.art{position:absolute;left:0;top:0;width:1098px;height:517px}
  .abs{position:absolute}
  .heading{font-weight:600;color:var(--ink);letter-spacing:.3px;line-height:1}
  .copy{font-size:7.3px;line-height:11px;text-align:justify}
  .copy p+p{margin-top:11px}
  .company-title{left:19px;top:150px;font-size:22px}
  .company-copy{left:17px;top:187px;width:339px}
  .cover-monogram{left:396px;top:214px;width:181px;text-align:center;font-size:58px;font-weight:600;color:var(--mark-grey);letter-spacing:2px;line-height:1}
  .cover-name{left:384px;top:333px;width:205px;text-align:center;font-size:11.5px;color:var(--mark-grey)}
  .cover-wordmark{left:751px;top:36px;font-size:42px;font-weight:600;color:#000;line-height:1;letter-spacing:.5px}
  .office{top:444px;font-size:8.3px;line-height:11px;color:#3a3a40}
  .office--milano{left:385px}
  .office--arco{left:563px}
  .office h3{font-size:10px;font-weight:600;color:var(--red);margin-bottom:3px;letter-spacing:.2px}
  .office li{list-style:none;display:flex;align-items:center;gap:4px}
  .office li.indent{padding-left:12px}
  .office svg{width:8px;height:8px;flex:none}
  .office-divider{left:549px;top:446px;width:1px;height:58px;background:#c9c9cc}
  .web-tab{left:733px;top:492px;width:154px;height:16px}
  .web-tab span{position:absolute;left:30px;top:3px;font-size:8px;color:#fff;letter-spacing:.2px}
  .print-date{left:15px;top:351px;font-size:5px;color:#555;letter-spacing:.1px}
  .pocket-wordmark{left:0;top:405px;width:346px;text-align:center;font-size:40px;font-weight:600;color:var(--mark-grey);line-height:1;letter-spacing:.5px}
  .pocket-slogan{left:0;top:460px;width:346px;text-align:center;font-size:11px;font-style:italic;color:#fff}
  .experience-title{left:382px;top:155px;font-size:16px}
  .experience-copy{left:382px;top:176px;width:338px}
  .founders-tab{left:387px;top:241px;font-size:6.8px;color:#fff;letter-spacing:.2px}
  .founders{left:382px;top:262px;width:338px}
  .founder h4{font-size:7px;font-weight:600;color:var(--red);line-height:9px}
  .founder p{font-size:6.8px;line-height:8.6px;text-align:justify;color:#333}
  .founder+.founder{margin-top:6px}
  .services-title{left:774px;top:18px;font-size:21px;color:#fff}
  .services-copy{left:774px;top:48px;width:310px;font-size:7.2px;line-height:11px;color:#e6e6ea;text-align:justify}
  .services-copy p+p{margin-top:11px}
  .services-list{left:746px;top:180px;width:341px;font-size:7.3px;line-height:10px;color:var(--body)}
  .services-list p{position:absolute;left:0;width:341px}
</style>
</head>
<body>
<main class="canvas">

  <section class="spread spread--outer" aria-label="Fronte esterno">
    <svg class="art" viewBox="0 0 1098 517">
      <defs>
        <linearGradient id="tunnelRock" x1="0" y1="0" x2="1" y2="1">
          <stop offset="0" stop-color="#6f6a58"/><stop offset=".5" stop-color="#8e7a5e"/><stop offset="1" stop-color="#a59d89"/>
        </linearGradient>
        <linearGradient id="siteAerial" x1="0" y1="0" x2="1" y2="1">
          <stop offset="0" stop-color="#9c968c"/><stop offset=".5" stop-color="#7d746a"/><stop offset="1" stop-color="#a8a095"/>
        </linearGradient>
        <linearGradient id="darkTunnel" x1="0" y1="0" x2="0" y2="1">
          <stop offset="0" stop-color="#3a3a3a"/><stop offset="1" stop-color="#111"/>
        </linearGradient>
        <linearGradient id="townSite" x1="0" y1="0" x2="0" y2="1">
          <stop offset="0" stop-color="#b7c3cf"/><stop offset="1" stop-color="#9a8673"/>
        </linearGradient>
        <linearGradient id="slopeSite" x1="0" y1="0" x2="1" y2="1">
          <stop offset="0" stop-color="#6f8a4f"/><stop offset=".6" stop-color="#a6a29a"/><stop offset="1" stop-color="#8f9a7a"/>
        </linearGradient>
        <linearGradient id="craneBlue" x1="0" y1="0" x2="1" y2="1">
          <stop offset="0" stop-color="#3a6fb0"/><stop offset=".6" stop-color="#c8403a"/><stop offset="1" stop-color="#7a7f88"/>
        </linearGradient>
        <linearGradient id="yardGrey" x1="0" y1="0" x2="1" y2="1">
          <stop offset="0" stop-color="#a9aaa9"/><stop offset=".6" stop-color="#8f8478"/><stop offset="1" stop-color="#b08060"/>
        </linearGradient>
        <linearGradient id="portalSite" x1="0" y1="0" x2="0" y2="1">
          <stop offset="0" stop-color="#b9c6d6"/><stop offset=".5" stop-color="#8c7d68"/><stop offset="1" stop-color="#6e6455"/>
        </linearGradient>
        <linearGradient id="pageShade" x1="0" y1="0" x2="1" y2="0">
          <stop offset="0" stop-color="#fff" stop-opacity="0"/><stop offset="1" stop-color="#e9e9ec"/>
        </linearGradient>
      </defs>

      <rect x="0" y="0" width="366" height="517" fill="url(#pageShade)"/>
      <rect role="img" aria-label="Foto: fronte di scavo di una galleria con operaio" x="0" y="0" width="366" height="138" fill="url(#tunnelRock)"/>
      <rect x="0" y="505" width="366" height="12" fill="var(--navy)"/>

      <polygon role="img" aria-label="Foto: fresa meccanica sollevata da gru" points="84,380 125.6,404 125.6,452 84,476 42.4,452 42.4,404" fill="url(#craneBlue)"/>
      <polygon role="img" aria-label="Foto: cantiere visto dall'alto" points="187,371 236.4,399.5 236.4,456.5 187,485 137.6,456.5 137.6,399.5" fill="url(#yardGrey)"/>
      <polygon role="img" aria-label="Foto: imbocchi di galleria in costruzione" points="291,380 332.6,404 332.6,452 291,476 249.4,452 249.4,404" fill="url(#portalSite)"/>

      <rect x="366" y="82" width="732" height="346" fill="var(--navy)"/>
      <rect x="732" y="82" width="366" height="13" fill="var(--navy-soft)"/>

      <rect role="img" aria-label="Foto: cantiere di grande opera visto dall'alto con gru" x="610" y="95" width="488" height="319" fill="url(#siteAerial)"/>

      <polygon role="img" aria-label="Foto: interno di galleria illuminata" points="977,305 1014.2,326.5 1014.2,369.5 977,391 939.8,369.5 939.8,326.5" fill="url(#darkTunnel)" stroke="#fff" stroke-width="2"/>
      <polygon role="img" aria-label="Foto: opere di sostegno in area urbana" points="934,388 971.2,409.5 971.2,452.5 934,474 896.8,452.5 896.8,409.5" fill="url(#townSite)" stroke="#fff" stroke-width="2"/>
      <polygon role="img" aria-label="Foto: versante consolidato lungo una strada" points="1037,376 1090.7,407 1090.7,469 1037,500 983.3,469 983.3,407" fill="url(#slopeSite)" stroke="#fff" stroke-width="2"/>
    </svg>

    <h2 class="abs heading company-title">OUR COMPANY</h2>
    <div class="abs copy company-copy">
      <p>TALVI Engineering S.r.l. offre servizi di consulenza tecnica, contrattuale e strategica ai principali attori nei settori delle scienze geologiche, dell’ingegneria geotecnica e dell’ingegneria idraulica. Lavoriamo per mitigare il rischio e ridurre l’incertezza, con flessibilità nella ricerca della soluzione ottimale contribuendo ad aumentare la redditività del progetto.</p>
      <p>TALVI Engineering S.r.l. è una società indipendente che nasce nel luglio 2020 dall’associazione di un gruppo di professionisti che hanno messo a fattor comune la reciproca esperienza maturata in oltre trent’anni di attività come progettisti e consulenti nel settore delle grandi opere di ingegneria civile lavorando come Direttori Tecnici di Main Engineering Companies and as Freelancers.</p>
      <p>Talvi Engineering S.r.l. vuole unire l’esperienza dei Fondatori e delle figure chiave con l’entusiasmo di chi intraprende una nuova attività, per dare vita ad una nuova realtà che si pone come obbiettivo principale il design of infrastructures that are safe, sustainable and economic.<br>Each of our projects represents a long term commitment, we believe in providing safe, reliable, sustainable end innovative solutions. This is and will be our distinctive characteristic.</p>
    </div>

    <div class="abs cover-monogram">TALVI</div>
    <div class="abs cover-name">TALVI Engineering S.r.l.</div>
    <div class="abs cover-wordmark">talvi</div>

    <div class="abs office office--milano">
      <h3>MILANO</h3>
      <ul>
        <li><svg viewBox="0 0 10 10"><path d="M5 0.5a3.3 3.3 0 0 0-3.3 3.3C1.7 6.3 5 9.5 5 9.5s3.3-3.2 3.3-5.7A3.3 3.3 0 0 0 5 .5Zm0 4.6a1.3 1.3 0 1 1 0-2.6 1.3 1.3 0 0 1 0 2.6Z" fill="var(--red)"/></svg>Via Lentisco, 14</li>
        <li class="indent">20121 Milano - IT</li>
        <li><svg viewBox="0 0 10 10"><path d="M2.2.8 3.8 2.6 3 4c.6 1.3 1.6 2.3 3 3l1.4-.8 1.8 1.6-.9 1.5C4.6 9 1 5.4.7 1.7Z" fill="var(--red)"/></svg>+39 02 555010101</li>
        <li><svg viewBox="0 0 10 10"><rect x=".5" y="2" width="9" height="6" fill="var(--red)"/><path d="M.5 2 5 5.5 9.5 2" fill="none" stroke="#fff" stroke-width=".8"/></svg>info@talviengineering.org</li>
      </ul>
    </div>
    <div class="abs office-divider"></div>
    <div class="abs office office--arco">
      <h3>ARCO TN</h3>
      <ul>
        <li><svg viewBox="0 0 10 10"><path d="M5 0.5a3.3 3.3 0 0 0-3.3 3.3C1.7 6.3 5 9.5 5 9.5s3.3-3.2 3.3-5.7A3.3 3.3 0 0 0 5 .5Zm0 4.6a1.3 1.3 0 1 1 0-2.6 1.3 1.3 0 0 1 0 2.6Z" fill="var(--red)"/></svg>Via dei Larici, 9</li>
        <li class="indent">38062 Arco TN - IT</li>
        <li><svg viewBox="0 0 10 10"><path d="M2.2.8 3.8 2.6 3 4c.6 1.3 1.6 2.3 3 3l1.4-.8 1.8 1.6-.9 1.5C4.6 9 1 5.4.7 1.7Z" fill="var(--red)"/></svg>+39 02 555010101</li>
        <li><svg viewBox="0 0 10 10"><rect x=".5" y="2" width="9" height="6" fill="var(--red)"/><path d="M.5 2 5 5.5 9.5 2" fill="none" stroke="#fff" stroke-width=".8"/></svg>info@talviengineering.org</li>
      </ul>
    </div>

    <div class="abs web-tab">
      <svg width="154" height="16" viewBox="0 0 154 16" aria-hidden="true">
        <polygon points="0,0 143,0 154,16 0,16" fill="var(--red)"/>
        <circle cx="20" cy="8" r="3.6" fill="none" stroke="#fff" stroke-width=".8"/>
        <path d="M16.4 8h7.2M20 4.4c-1.6 2-1.6 5.2 0 7.2M20 4.4c1.6 2 1.6 5.2 0 7.2" fill="none" stroke="#fff" stroke-width=".7"/>
      </svg>
      <span>www.talviengineering.org</span>
    </div>
  </section>

  <section class="spread spread--inner" aria-label="Interno">
    <svg class="art" viewBox="0 0 1098 517">
      <defs>
        <linearGradient id="fadedSite" x1="0" y1="0" x2="1" y2="1">
          <stop offset="0" stop-color="#e9e9eb"/><stop offset=".5" stop-color="#d6d6d9"/><stop offset="1" stop-color="#e4e4e6"/>
        </linearGradient>
        <linearGradient id="pocketPanel" x1="0" y1="0" x2="1" y2="1">
          <stop offset="0" stop-color="#353744"/><stop offset="1" stop-color="#22232d"/>
        </linearGradient>
        <linearGradient id="tunnelWorks" x1="0" y1="0" x2="1" y2="0">
          <stop offset="0" stop-color="#9aa0a6"/><stop offset=".45" stop-color="#4a4640"/><stop offset=".6" stop-color="#c46a2e"/><stop offset="1" stop-color="#5b5a52"/>
        </linearGradient>
        <linearGradient id="groundBand" x1="0" y1="0" x2="1" y2="0">
          <stop offset="0" stop-color="#4c4f5b"/><stop offset=".5" stop-color="#6b6e78"/><stop offset="1" stop-color="#50535e"/>
        </linearGradient>
        <linearGradient id="teamTone" x1="0" y1="0" x2="0" y2="1">
          <stop offset="0" stop-color="#e8e8ea"/><stop offset="1" stop-color="#8d8f97"/>
        </linearGradient>
      </defs>

      <rect role="img" aria-label="Foto schiarita: scavo con paratie visto dall'alto" x="0" y="0" width="366" height="517" fill="url(#fadedSite)"/>
      <polygon points="0,365 347,365 366,517 0,517" fill="url(#pocketPanel)"/>

      <rect x="732" y="0" width="366" height="138" fill="var(--navy)"/>

      <rect role="img" aria-label="Foto: escavatore e macchinari al fronte di una galleria" x="366" y="9" width="366" height="127" fill="url(#tunnelWorks)"/>

      <polygon points="381,238 524,238 536,253 381,253" fill="var(--navy)"/>

      <rect role="img" aria-label="Foto: cantiere con mezzi e paratie, toni scuri" x="366" y="442" width="732" height="75" fill="url(#groundBand)"/>

      <polygon role="img" aria-label="Foto del team dei soci fondatori" points="677,414 718.6,438 718.6,486 677,510 635.4,486 635.4,438" fill="url(#teamTone)" stroke="#fff" stroke-width="2.5"/>
    </svg>

    <div class="abs print-date">BROCHURE PRINTED IN DATA gg/mm/aaaa</div>
    <div class="abs pocket-wordmark">talvi</div>
    <div class="abs pocket-slogan">… talvi engineering … reliable solutions …</div>

    <h2 class="abs heading experience-title">OUR EXPERIENCE AND EXPERTISE</h2>
    <div class="abs copy experience-copy">
      <p>La società nasce dall’associazione di un gruppo di professionisti, con indiscusse competenze ed affidabilità, con esperienza maturata in oltre trent’anni di attività come progettisti e consulenti nel settore delle grandi opere di ingegneria civile; geologia, ingegneria geotecnica ed idraulica ed opere sotterranee sono il “core” delle loro competenze ….</p>
    </div>
    <div class="abs founders-tab">I SOCI FONDATORI SONO:</div>
    <div class="abs founders">
      <div class="founder">
        <h4>MARCO</h4>
        <p>Marco, 30 anni di esperienza professionale. Coinvolto in oltre 150 gallerie naturali per più di 360 km. Numerosi progetti di assistenza tecnica su strutture, versanti e opere di protezione ambientale. Negli ultimi dieci anni responsabile di assistenza in corso d’opera e progettazione esecutiva. Opere per oltre 1.400 Mio EUR.</p>
      </div>
      <div class="founder">
        <h4>GIULIA</h4>
        <p>Giulia, 30 anni di esperienza professionale. Coinvolta in oltre 150 gallerie naturali per più di 360 km. Numerosi progetti di assistenza tecnica su strutture, versanti e opere di protezione ambientale. Negli ultimi dieci anni responsabile di assistenza in corso d’opera e progettazione esecutiva. Opere per oltre 1.400 Mio EUR.</p>
      </div>
      <div class="founder">
        <h4>SERENA</h4>
        <p>Serena, 30 anni di esperienza professionale. Coinvolta in oltre 150 gallerie naturali per più di 360 km. Numerosi progetti di assistenza tecnica su strutture, versanti e opere di protezione ambientale. Negli ultimi dieci anni responsabile di assistenza in corso d’opera e progettazione esecutiva. Opere per oltre 1.400 Mio EUR.</p>
      </div>
    </div>

    <h2 class="abs heading services-title">OUR SERVICES</h2>
    <div class="abs services-copy">
      <p>Progettazione e consulenza specialistica nel campo della geologia, dell’ingegneria geotecnica, delle opere sotterranee e dell’ingegneria idtraulica.</p>
      <p>Aiutiamo i nostri clienti a risolvere problemi di natura progettuale, contrattuale e costruttiva che possono nascere nell’intera vita del progetto portando la nostra esperienza all’interno delle loro organizzazioni, migliorando la qualità dei loro servizi di ingegneria, ottimizzando i loro progetti, proponendo nuove idee e soluzioni, rafforzando i loro approcci ……</p>
    </div>
    <div class="abs services-list">
      <p style="top:0;text-align:justify;line-height:11px">Talvi Engineering è in grado di fornire la propria assistenza nell’intero iter procedurale, dalla fase di indagine preliminare e di analisi di fattibilità fino alla progettazione costruttiva e all’assistenza tecnica in fase realizzativa.</p>
      <p style="top:46px;line-height:11px">La specializzazione e l’esperienza accumulate nelle discipline della geologia, dell’ingegneria geotecnica e del sottosuolo e dell’idraulica ci permette di massimizzare la nostra efficacia quando sia necessario:</p>
      <p style="top:90px">Far fronte a situazioni di emergenza anche su progetti in fase di sviluppo avanzato garantendo l’immediata focalizzazione delle problematiche di progetto e garantendo il risultato finale atteso (in termini di qualità, tempistiche e costi…)</p>
      <p style="top:136px">Fornire “second opinion” di elevato valore tecnico ed amministrativo in occasione di problematiche progettuali e costruttive e dispute legali</p>
      <p style="top:175px">Analizzare in tempi brevi progetti svolti da terzi individuandone le “criticità”, verificandone la cantierabilità e la validità tecnico economica</p>
      <p style="top:207px;width:190px">Ottimizzare i progetti redatti da terzi implementandone il contenuto e massimizzando l’efficacia economica degli investimenti.</p>
    </div>
  </section>

</main>
</body>
</html>
```